The Brightwater Compass Business Card

We need an attractive business card with the logo that we bought from ArtVantly last year.
Our mission is to contribute to change the way today's leaders manage business companies bringing value to the workplace and helping them to build a new model of creating wealth.
Our logo is clear about our values : we seek Positive Change through People and are convinced that the pursuit of individual well-being and the chase of economic results can converge with the right management.
Management Consulting
Corinne Fabrelle
+34 612 98 70 31
corinne.fabrelle@thebrightwatercompass-mail.net
www.thebrightwatercompass-mail.net

```html
<!DOCTYPE html>
<html lang="en">
<head>
<meta charset="utf-8">
<title>The Brightwater Compass – Business Card</title>
<link rel="stylesheet" href="https://fonts.googleapis.com/css2?family=Noto+Sans:wght@400;700&display=swap">
<style>
  :root {
    --canvas-bg: #f1f2f2;
    --canvas-edge: #dcdddd;
    --card-black: #141414;
    --card-teal: #138481;
    --brand-teal: #1f8f8b;
    --text-teal: #4fb3ae;
    --text-soft: #7fbfbb;
    --tree-white: #f4f8f7;
  }
  html, body {
    margin: 0;
    padding: 0;
    width: 1200px;
    height: 1000px;
    overflow: hidden;
  }
  body {
    background: radial-gradient(ellipse at 50% 45%, var(--canvas-bg) 40%, var(--canvas-edge) 100%);
    font-family: "Noto Sans", Arial, sans-serif;
    position: relative;
  }
  .card {
    position: absolute;
    width: 560px;
    height: 320px;
    border-radius: 22px;
    box-shadow: 0 6px 14px rgba(0,0,0,0.25);
    overflow: hidden;
  }
  .card-front {
    left: 200px;
    top: 180px;
    background: var(--card-black);
  }
  .card-back {
    left: 420px;
    top: 500px;
    background: var(--card-teal);
  }
  .brand {
    position: absolute;
    top: 70px;
    right: 60px;
    display: flex;
    align-items: center;
    gap: 12px;
  }
  .brand-dot {
    width: 18px;
    height: 18px;
    border-radius: 50%;
    background: var(--brand-teal);
  }
  .brand-name {
    margin: 0;
    font-size: 26px;
    font-weight: 700;
    color: var(--brand-teal);
    line-height: 1;
  }
  .brand-tagline {
    position: absolute;
    top: 112px;
    right: 60px;
    margin: 0;
    font-size: 11px;
    letter-spacing: 5px;
    color: var(--brand-teal);
    text-transform: uppercase;
  }
  .contact {
    position: absolute;
    left: 40px;
    bottom: 34px;
  }
  .contact-name {
    margin: 0 0 4px;
    font-size: 19px;
    font-weight: 700;
    color: var(--text-teal);
  }
  .contact-line {
    margin: 0;
    font-size: 13px;
    line-height: 17px;
    color: var(--text-soft);
  }
  .contact-gap { margin-top: 16px; }
  .tree-area {
    position: absolute;
    left: 110px;
    top: 70px;
    width: 400px;
    height: 250px;
    border-radius: 200px 200px 0 0;
    background: radial-gradient(ellipse at 50% 55%, var(--tree-white) 0%, rgba(244,248,247,0.85) 55%, rgba(244,248,247,0) 100%);
  }
</style>
</head>
<body>
  <section class="card card-front">
    <div class="brand">
      <span class="brand-dot"></span>
      <h1 class="brand-name">The Brightwater Compass</h1>
    </div>
    <p class="brand-tagline">Management Consulting</p>
    <div class="contact">
      <p class="contact-name">Corinne Fabrelle</p>
      <p class="contact-line">+34 612 98 70 31</p>
      <p class="contact-line contact-gap">corinne.fabrelle</p>
      <p class="contact-line">@thebrightwatercompass-mail.net</p>
      <p class="contact-line">www.thebrightwatercompass-mail.net</p>
    </div>
  </section>

  <section class="card card-back">
    <div class="tree-area" role="img" aria-label="Large white brand tree illustration on teal"></div>
  </section>
</body>
</html>
```